Bounty Bazaar 2022- FB poster ads

Design for our Bounty Bazaar Event
Designs 3 designs for Face Book Banner, posts and social Media ads
Each can look the same just different subjects on each
1. Design We're Back!
The Bounty Bazaar Is Back!
Ventura County’s Premier Food, Wine and Brew Event
August 14th
Vendor and ticket info at https://bountybazaarhub.com/

2. Vendors be a part of the event
The Bounty Bazaar is Back!
August 14th 2020
Vendors sign up today at
Vendor info at https://bountybazaarhub.com/

3. Sponsor info
The Bounty Bazaar
August 14th 2022
Check out our great Sponsorship opportunities
Sponsor info at https://bountybazaarhub.com/

Target Market(s)

Foodies, wine and beer enthusists

Industry/Entity Type

Farm to fork, fresh in season and local

Colors
00AB8E
00BBA5
67D7C9
C6EFE9
E9F9F6

Requirements
Should not have
• no fast food looking photos

```html
<!DOCTYPE html>
<html lang="en">
<head>
<meta charset="utf-8">
<title>Bounty Bazaar – We're Back</title>
<link rel="stylesheet" href="https://fonts.googleapis.com/css2?family=Saira+Condensed:wght@400;500&family=Great+Vibes&family=Cormorant+Garamond:wght@500&display=swap">
<style>
  :root {
    --frame: #000000;
    --teal: #00AB8E;
    --accent: #E0451C;
    --ink: #2b2b2b;
    --white: #ffffff;
    --sky-top: #eef0f2;
    --sky-low: #a9b4c0;
    --stage: #6d5a48;
    --food-light: #efe6dc;
    --food-warm: #e08a3c;
    --food-deep: #a9582a;
    --food-green: #9bb07a;
    --tent: #f1efea;
    --garden: #8f9a7c;
    --shirt: #2a2a2c;
    --table-red: #b0443d;
  }
  html, body { margin: 0; padding: 0; overflow: hidden; }
  body { width: 1200px; height: 1198px; background: var(--frame); position: relative; font-family: "Saira Condensed", sans-serif; }
  .poster { position: absolute; left: 110px; top: 99px; width: 980px; height: 999px; background: var(--teal); overflow: hidden; }
  .photo-layer { position: absolute; inset: 0; }
  .poster p { margin: 0; }
  .event-title { position: absolute; left: 430px; top: 52px; width: 520px; margin: 0; text-align: center; color: var(--white); line-height: 1; font-weight: normal; text-shadow: 0 1px 6px rgba(80, 40, 10, 0.35); }
  .event-title .big { display: block; font-family: "Cormorant Garamond", serif; font-weight: 500; font-size: 128px; letter-spacing: 1px; }
  .event-title .script { display: block; font-family: "Great Vibes", cursive; font-size: 118px; margin-top: -6px; }
  .brand { position: absolute; left: 176px; top: 420px; width: 180px; height: 96px; display: flex; align-items: center; justify-content: center; gap: 8px; }
  .brand-dot { width: 16px; height: 16px; border-radius: 50%; background: var(--accent); }
  .brand-name { font-family: "Saira Condensed", sans-serif; font-weight: 500; font-size: 30px; color: var(--accent); }
  .headline { position: absolute; left: 68px; top: 512px; width: 400px; margin: 0; text-align: center; color: var(--accent); font-weight: 400; font-size: 54px; line-height: 56px; text-transform: uppercase; }
  .tagline { position: absolute; left: 48px; top: 716px; width: 440px; text-align: center; color: var(--white); font-family: "Great Vibes", cursive; font-size: 56px; line-height: 1.06; }
  .date { position: absolute; left: 68px; top: 871px; width: 400px; text-align: center; color: var(--ink); font-size: 31px; line-height: 1; }
  .date sup { font-size: 12px; vertical-align: 16px; }
  .subtitle { position: absolute; left: 28px; top: 903px; width: 480px; text-align: center; color: var(--white); font-size: 20px; }
  .info { position: absolute; left: 28px; top: 937px; width: 480px; text-align: center; color: var(--ink); font-size: 18.5px; }
</style>
</head>
<body>
  <main class="poster">
    <svg class="photo-layer" width="980" height="999" viewBox="0 0 980 999">
      <defs>
        <clipPath id="photo-area"><polygon points="104,0 980,0 980,999 809,999"/></clipPath>
        <linearGradient id="stage-tone" x1="0" y1="0" x2="0" y2="1">
          <stop offset="0" stop-color="var(--sky-top)"/>
          <stop offset="0.6" stop-color="var(--sky-low)"/>
          <stop offset="1" stop-color="var(--stage)"/>
        </linearGradient>
        <linearGradient id="food-tone" x1="0" y1="0" x2="1" y2="1">
          <stop offset="0" stop-color="var(--food-light)"/>
          <stop offset="0.35" stop-color="var(--food-warm)"/>
          <stop offset="0.7" stop-color="var(--food-green)"/>
          <stop offset="1" stop-color="var(--food-deep)"/>
        </linearGradient>
        <linearGradient id="food-low-tone" x1="0" y1="0" x2="0" y2="1">
          <stop offset="0" stop-color="var(--food-light)"/>
          <stop offset="0.35" stop-color="var(--food-warm)"/>
          <stop offset="0.65" stop-color="var(--food-green)"/>
          <stop offset="1" stop-color="var(--food-light)"/>
        </linearGradient>
        <linearGradient id="guest-tone" x1="0" y1="0" x2="0" y2="1">
          <stop offset="0" stop-color="var(--tent)"/>
          <stop offset="0.45" stop-color="var(--garden)"/>
          <stop offset="0.75" stop-color="var(--table-red)"/>
          <stop offset="1" stop-color="var(--shirt)"/>
        </linearGradient>
      </defs>
      <g clip-path="url(#photo-area)">
        <rect x="104" y="0" width="876" height="391" fill="url(#food-tone)" role="img" aria-label="Photo of ceviche served in glasses with tortilla chips"/>
        <rect x="104" y="0" width="310" height="200" fill="url(#stage-tone)" role="img" aria-label="Photo of two musicians performing on an outdoor stage"/>
        <rect x="399" y="391" width="242" height="608" fill="url(#food-low-tone)" role="img" aria-label="Photo of ceviche appetizers in martini glasses"/>
        <rect x="641" y="391" width="339" height="608" fill="url(#guest-tone)" role="img" aria-label="Photo of a vendor raising a glass of beer at the event"/>
        <line x1="399" y1="391" x2="980" y2="391" stroke="var(--white)" stroke-width="2"/>
        <line x1="641" y1="391" x2="641" y2="999" stroke="var(--white)" stroke-width="2"/>
      </g>
    </svg>

    <h1 class="event-title"><span class="big">BOUNTY</span><span class="script">Bazaar</span></h1>

    <div class="brand"><span class="brand-dot"></span><span class="brand-name">Fieldline VC</span></div>

    <h2 class="headline">Design<br>We're Back!</h2>
    <p class="tagline">The Bounty Bazaar<br>is Back</p>
    <p class="date">AUGUST 14<sup>TH</sup>, 2022</p>
    <p class="subtitle">Ventura County’s Premier Food, Wine and Brew Event</p>
    <p class="info">VENDOR AND TICKET INFO AT https://bountybazaarhub.com/</p>
  </main>
</body>
</html>
```